We need a DL size flyer, double sided, for our lawn mowing and gardening business, Kestrel Greens.

We want to run on the front side, the following promotion:
50% off lawn mowing, applies to first lawn mowed on any regular service,
applies to first 100 callers only, so call now!
Professional lawn mowing at an affordable price.

Logo at the bottom left, with Lawn and Garden Maintenance written just below logo.

On bottom Right contact details;
Tom and Gareth
Ph: 0487650912
Email: kestrelgreens@mailbox-example.com
www.kestrelgreens-example.com.au

Front side positioned horizontally, with a bright and colour full design in the background, with the offer of 50% Off lawn mowing in large letters along the top.

On the rear side, also positioned horizontally, a list of our services, stating;

At Kestrel Greens we specialise in the following services;
Lawn mowing
Edging
Blowing
Hedging
Pruning
Tree Loping
Weeding
Poisoning
Mulching
Fertilising
Rubbish removal
Planting
Lawn care and advice
Turf
And any other garden maintenance job,
No job too big or too small.
(No particular order, whatever fits best)
Also include our contact details,
Kestrel Greens
Ph 0487650912
www.kestrelgreens-example.com.au

Target Market(s)

Home owners, aged between 30-50 years old, moderate socio ecenomic status to more afluent areas.

Industry/Entity Type

Business

Requirements
Must have
• DL size, front and back, full colour.
Nice to have
• The writting stating "Kestrel Greens" in our logo is quite bland, if that could also be amended to make it more appealing, but change the writting design only not the actual logo.

```html
<!DOCTYPE html>
<html lang="en">
<head>
<meta charset="utf-8">
<title>Kestrel Greens – DL Flyer</title>
<link rel="stylesheet" href="https://fonts.googleapis.com/css2?family=Arvo:wght@700&family=Dosis:wght@500&family=Open+Sans:wght@700&family=Tinos&display=swap">
<style>
  :root {
    --green: #0e9a0e;
    --green-dark: #0a7f0a;
    --grass-light: #8fd14a;
    --grass-mid: #4caf1e;
    --grass-deep: #2f8a12;
    --ink: #1f1f1f;
    --white: #ffffff;
    --bg-top: #7a7a7a;
    --bg-mid: #e4e4e4;
    --bg-bottom: #7d7d7d;
  }
  * { margin: 0; padding: 0; box-sizing: border-box; }
  html, body { width: 1200px; height: 895px; overflow: hidden; }
  body {
    position: relative;
    background: linear-gradient(180deg, var(--bg-top) 0%, var(--bg-mid) 30%, var(--bg-mid) 62%, var(--bg-bottom) 100%);
  }
  .panel {
    position: absolute;
    top: 109px;
    height: 576px;
    background: var(--white);
    overflow: hidden;
    box-shadow: 0 0 30px 12px rgba(255,255,255,0.85);
  }
  .panel--front { left: 44px; width: 561px; }
  .panel--back { left: 627px; width: 534px; }
  .band-top { position: absolute; left: 0; top: 0; right: 0; height: 12px; background: var(--green); }
  .band-bottom { position: absolute; left: 0; bottom: 0; right: 0; height: 40px; background: var(--green); }
  .grass {
    position: absolute; left: 0; right: 0; top: 330px; height: 190px;
    background: linear-gradient(180deg, rgba(143,209,74,0) 0%, var(--grass-light) 30%, var(--grass-mid) 60%, var(--grass-deep) 100%);
  }
  .panel--front .grass {
    background:
      linear-gradient(90deg, rgba(255,255,255,0.75) 0%, rgba(255,255,255,0) 55%),
      linear-gradient(180deg, rgba(143,209,74,0) 0%, var(--grass-light) 38%, var(--grass-mid) 65%, var(--grass-deep) 100%);
  }
  .promo {
    position: absolute; left: 24px; top: 34px;
    font-family: "Tinos", "Times New Roman", serif;
    font-size: 16.5px; line-height: 24.5px; color: var(--green-dark);
  }
  .promo .tagline { margin-left: -2px; }
  .offer-badge { position: absolute; left: 367px; top: 159px; width: 192px; height: 192px; z-index: 2; }
  .offer-badge text { font-family: "Open Sans", Arial, sans-serif; font-weight: 700; fill: var(--white); }
  .brand {
    position: absolute; left: 62px; top: 490px; z-index: 2;
    display: flex; align-items: center; gap: 8px;
    font-family: "Open Sans", Arial, sans-serif; font-weight: 700;
    font-size: 22px; line-height: 30px; color: var(--ink);
    background: var(--white); padding: 2px 12px;
  }
  .brand__mark { width: 12px; height: 12px; background: var(--green); }
  .brand-strap {
    position: absolute; left: 39px; bottom: 10px;
    font-family: "Arvo", Georgia, serif; font-weight: 700;
    font-size: 12.5px; color: var(--white); letter-spacing: 0.2px;
  }
  .contact {
    position: absolute; left: 310px; top: 418px;
    font-family: "Tinos", "Times New Roman", serif; color: var(--white);
    text-shadow: 0 0 2px rgba(0,0,0,0.35);
    white-space: nowrap;
  }
  .contact h3 { font-weight: 400; font-size: 16px; line-height: 20px; }
  .contact p { font-size: 12.6px; line-height: 15px; padding-left: 12px; }
  .services-intro {
    position: absolute; left: 9px; top: 34px;
    font-family: "Dosis", Arial, sans-serif; font-weight: 500;
    font-size: 17.5px; color: var(--green-dark);
  }
  .service-list {
    position: absolute; list-style: none;
    font-family: "Dosis", Arial, sans-serif; font-weight: 500;
    font-size: 17px; line-height: 22.8px; color: var(--green);
  }
  .service-list li::before { content: "•"; }
  .service-list--main { left: 49px; top: 66px; }
  .service-list--extra { left: 241px; top: 64px; }
  .contact-box {
    position: absolute; right: 0; top: 329px; width: 261px; height: 82px;
    background: var(--green); padding: 6px 0 0 15px;
    font-family: "Tinos", "Times New Roman", serif; font-size: 17.5px; line-height: 24px; color: var(--white);
    white-space: nowrap;
  }
  .contact-box .web { font-size: 15px; }
</style>
</head>
<body>

<section class="panel panel--front" aria-label="Flyer front">
  <div class="band-top"></div>
  <div class="grass" role="img" aria-label="Close-up photograph of bright green lawn grass"></div>
  <div class="promo">
    <p>50% off lawn mowing, applies to first lawn mowed on any regular service,</p>
    <p>applies to first 100 callers only, so call now!</p>
    <p class="tagline">Professional lawn mowing at an affordable price.</p>
  </div>
  <svg class="offer-badge" viewBox="0 0 192 192" aria-label="50% Off Lawn mowing">
    <circle cx="96" cy="96" r="91" fill="var(--white)" stroke="var(--green)" stroke-width="8"/>
    <circle cx="96" cy="96" r="76" fill="var(--green)"/>
    <text x="96" y="90" text-anchor="middle" font-size="20">50% Off</text>
    <text x="96" y="115" text-anchor="middle" font-size="19">Lawn mowing</text>
  </svg>
  <div class="brand"><span class="brand__mark"></span>Kestrel Greens</div>
  <div class="contact">
    <h3>Contact details:</h3>
    <p>Tom and Gareth</p>
    <p>Ph: 0487650912</p>
    <p>Email: kestrelgreens@mailbox-example.com</p>
    <p>www.kestrelgreens-example.com.au</p>
  </div>
  <div class="band-bottom"></div>
  <p class="brand-strap">Lawn &amp; Garden Maintenance</p>
</section>

<section class="panel panel--back" aria-label="Flyer back">
  <div class="band-top"></div>
  <div class="grass" role="img" aria-label="Photograph of a green grass bank"></div>
  <p class="services-intro">At Kestrel Greens we specialise in the following services;</p>
  <ul class="service-list service-list--main">
    <li>Lawn mowing</li><li>Edging</li><li>Blowing</li><li>Hedging</li><li>Pruning</li><li>Tree Loping</li>
    <li>Weeding</li><li>Poisoning</li><li>Mulching</li><li>Fertilising</li><li>Rubbish Removal</li><li>Planting</li>
  </ul>
  <ul class="service-list service-list--extra">
    <li>Lawn care and Advice</li><li>Turf</li><li>And other garden maintenance</li>
  </ul>
  <div class="contact-box">
    <p>Kestrel Greens</p>
    <p>Ph 0487650912</p>
    <p class="web">www.kestrelgreens-example.com.au</p>
  </div>
  <div class="band-bottom"></div>
</section>

</body>
</html>
```